Exciting new branding of Recruitment Company based on it's new website

We have an exciting new website we are about to launch and would like to have letterhead, business cards, email signature options, email banner, linkedin and facebook cover images all refreshed to match the website. I have attached the existing logo. The website is at http://brightcrewstaff.hostpadsites.com/ and we are particularly interested in the grey with orange writing at the base of the first page where it says Register Now

Target Market(s)

Recruitment

Contact Information for Business Card

Dana Thorpe
Account Executive
T: 1300 582 318
M: 0412 736 085
E: dana@brightcrewstaff.com.au
W: brightcrewstaff.com.au
A: Suite 3, 42 Wattlebank Lane, Deakin ACT 2600
ABN: 52 184 637 905

Font styles to use
Serif
Sans Serif

Requirements
Must have
• The grey colour from the website

```html
<!DOCTYPE html>
<html lang="en">
<head>
<meta charset="utf-8">
<title>bright crew – stationery</title>
<link rel="stylesheet" href="https://fonts.googleapis.com/css2?family=Lato:ital,wght@0,400;0,700;0,900;1,400&display=swap">
<style>
  :root {
    --orange: #f39322;
    --ink: #4a4a4a;
    --soft-ink: #6b6b6b;
    --paper: #ffffff;
    --card-black: #0c0c0d;
    --stage-top: #d9cfcc;
    --stage-bottom: #d2d2ce;
  }
  * { margin: 0; padding: 0; box-sizing: border-box; }
  html, body { width: 906px; height: 1200px; overflow: hidden; }
  body { font-family: "Lato", Arial, sans-serif; color: var(--ink); position: relative; }

  .stage-letterhead { position: absolute; left: 0; top: 0; width: 906px; height: 594px; background: var(--stage-top); }
  .stage-cards { position: absolute; left: 0; top: 594px; width: 906px; height: 606px; background: var(--stage-bottom); }

  /* Shared wordmark: stacked two-line name beside a plain circle */
  .brand { display: flex; align-items: center; gap: 8px; color: var(--orange); font-weight: 900; letter-spacing: -.3px; }
  .brand-name { display: flex; flex-direction: column; line-height: .92; }
  .brand-dot { border-radius: 50%; background: var(--orange); flex: none; }

  /* Letterhead */
  .letterhead {
    position: absolute; left: 262px; top: 28px; width: 382px; height: 540px;
    background: var(--paper); border-left: 6px solid var(--orange);
    box-shadow: 0 6px 18px rgba(0,0,0,.12);
    padding: 30px 30px 30px 40px;
  }
  .letterhead .brand { justify-content: flex-end; font-size: 17px; }
  .letterhead .brand-dot { width: 30px; height: 30px; }

  .letter-contact { margin-top: 12px; text-align: right; font-size: 6.4px; line-height: 1.55; color: var(--soft-ink); }
  .letter-contact .row { display: flex; justify-content: flex-end; align-items: center; gap: 4px; }
  .letter-contact .icon { width: 7px; height: 7px; }
  .letter-contact .abn-label { color: var(--orange); }

  .letter-body { margin-top: 20px; font-size: 7.6px; line-height: 1.6; color: var(--soft-ink); font-style: italic; }
  .letter-body p { margin-bottom: 9px; }
  .letter-body .salutation { margin-bottom: 12px; }
  .letter-signoff { margin-top: 14px; font-size: 7.6px; font-style: italic; color: var(--soft-ink); }
  .signature { display: block; margin-top: 6px; width: 34px; height: 14px; background: linear-gradient(90deg, rgba(243,147,34,.35), rgba(243,147,34,.15)); border-radius: 3px; }

  /* Business cards */
  .card {
    position: absolute; width: 380px; height: 236px;
    border-bottom: 4px solid var(--orange);
    box-shadow: 0 8px 20px rgba(0,0,0,.22);
  }
  .card-front { left: 48px; top: 660px; background: var(--paper); display: flex; align-items: center; padding: 0 22px; }
  .card-back { left: 478px; top: 900px; background: var(--card-black); display: flex; align-items: center; justify-content: center; }

  .card-front .brand { font-size: 20px; width: 138px; }
  .card-front .brand-dot { width: 40px; height: 40px; }
  .card-divider { width: 1.5px; height: 128px; background: var(--orange); margin: 0 16px 0 6px; }

  .card-details { font-size: 9.4px; line-height: 1.5; color: var(--soft-ink); }
  .holder-name { font-size: 19px; font-weight: 900; color: var(--orange); line-height: 1.05; }
  .holder-role { font-size: 10px; margin-bottom: 6px; color: var(--ink); }
  .card-details .row { display: flex; align-items: center; gap: 5px; }
  .card-details .icon { width: 9px; height: 9px; flex: none; }
  .card-details .address { padding-left: 14px; margin-bottom: 2px; }
  .card-details .abn { padding-left: 14px; }

  .card-back .brand { font-size: 36px; gap: 16px; }
  .card-back .brand-dot { width: 72px; height: 72px; }
</style>
</head>
<body>
<svg width="0" height="0" style="position:absolute" aria-hidden="true">
  <defs>
    <symbol id="icon-phone" viewBox="0 0 10 10"><rect x="0.5" y="0.5" width="9" height="9" rx="1.5" fill="#f39322"/><path d="M3 3.2c.6 2 1.6 3.1 3.6 3.8l.7-.9-1.1-.7-.5.4c-.7-.4-1.2-.9-1.6-1.6l.4-.5-.7-1.1z" fill="#fff"/></symbol>
    <symbol id="icon-mobile" viewBox="0 0 10 10"><rect x="1" y="2" width="8" height="6" rx="1" fill="none" stroke="#f39322" stroke-width="1.2"/></symbol>
    <symbol id="icon-mail" viewBox="0 0 10 10"><rect x="0.5" y="1.5" width="9" height="7" fill="#f39322"/><path d="M0.5 1.5 5 5.5l4.5-4M0.5 8.5 4 5M9.5 8.5 6 5" fill="none" stroke="#fff" stroke-width=".8"/></symbol>
    <symbol id="icon-web" viewBox="0 0 10 10"><circle cx="5" cy="5" r="4.4" fill="#f39322"/><path d="M.8 5h8.4M5 .6v8.8M2 2.6c2 1 4 1 6 0M2 7.4c2-1 4-1 6 0" fill="none" stroke="#fff" stroke-width=".6"/></symbol>
  </defs>
</svg>

<div class="stage-letterhead"></div>
<div class="stage-cards"></div>

<article class="letterhead">
  <div class="brand"><span class="brand-dot"></span><span class="brand-name"><span>bright</span><span>crew</span></span></div>

  <div class="letter-contact">
    <div>Suite 3, 42 Wattlebank Lane,</div>
    <div>Larrow Heights ACT 2699</div>
    <div class="row">1300 582 318 <svg class="icon"><use href="#icon-phone"/></svg></div>
    <div class="row">0412 736 085 <svg class="icon"><use href="#icon-mobile"/></svg></div>
    <div class="row">dana@brightcrewstaff.com.au <svg class="icon"><use href="#icon-mail"/></svg></div>
    <div class="row">www.brightcrewstaff.com.au <svg class="icon"><use href="#icon-web"/></svg></div>
    <div><span class="abn-label">ABN:</span> 52 184 637 905</div>
  </div>

  <div class="letter-body">
    <p class="salutation">Dear Sir/Mam,</p>
    <p>Contrary to popular belief, Lorem Ipsum is not simply random text. It has roots in a piece of classical Latin literature from 45 BC, making it over 2000 years old. Richard Holloway, a Latin professor at Harrowgate College in Vermont, looked up one of the more obscure Latin words, consectetur.</p>
    <p>Lorem Ipsum comes from sections 1.10.32 and 1.10.33 of "de Finibus Bonorum et Malorum" (The Extremes of Good and Evil) by Aurelian, written in 45 BC. This book is a treatise on the theory of ethics, very popular during the Renaissance. The first line of Lorem Ipsum.</p>
    <p>The standard chunk of Lorem Ipsum used since the 1500s is reproduced below for those interested. Sections 1.10.32 and 1.10.33 from "de Finibus Bonorum et Malorum" by Aurelian are also reproduced in their exact original.</p>
    <p>The standard chunk of Lorem Ipsum used since the 1500s is reproduced below for those interested.</p>
  </div>

  <div class="letter-signoff">
    Best Regards
    <span class="signature" role="img" aria-label="Handwritten signature"></span>
  </div>
</article>

<section class="card card-front">
  <div class="brand"><span class="brand-dot"></span><span class="brand-name"><span>bright</span><span>crew</span></span></div>
  <div class="card-divider"></div>
  <div class="card-details">
    <div class="holder-name">Dana Thorpe</div>
    <div class="holder-role">Account Executive</div>
    <div class="address">Suite 3, 42 Wattlebank Lane,<br>Larrow Heights ACT 2699</div>
    <div class="row"><svg class="icon"><use href="#icon-phone"/></svg>1300 582 318</div>
    <div class="row"><svg class="icon"><use href="#icon-mobile"/></svg>0412 736 085</div>
    <div class="row"><svg class="icon"><use href="#icon-mail"/></svg>dana@brightcrewstaff.com.au</div>
    <div class="row"><svg class="icon"><use href="#icon-web"/></svg>www.brightcrewstaff.com.au</div>
    <div class="abn">ABN: 52 184 637 905</div>
  </div>
</section>

<section class="card card-back">
  <div class="brand"><span class="brand-dot"></span><span class="brand-name"><span>bright</span><span>crew</span></span></div>
</section>
</body>
</html>
```